High-end residential home builder needs a business card design

We need a new business card design for a small residential construction company based in Boise, Idaho. We specialize in building custom high-end homes and remodels, with a focus on great design and craftsmanship.

We would like to use our current logo, but open to new color suggestions.
Just looking for a clean, sharp, modern design that looks high-end.

Target Market(s)

Upscale clientele

Industry/Entity Type

Contractor

Contact Information for Business Card

Company: Stonefield Custom Builders
Name: Marcus Tilley
Phone number: 208 367 4120
Email: MarcusTilleySCB@mailbox-example.com
Website: Stonefieldcustombuilders-example.com

Font styles to use
Serif
Sans Serif

Requirements
Must have
• Company Logo
Company name
My name
My phone number
My email
Company website
Nice to have
• I have attached a few photos of cards that I really like.

```html
<!DOCTYPE html>
<html lang="en">
<head>
<meta charset="utf-8">
<title>Stonefield Custom Builders — Business Card</title>
<link href="https://fonts.googleapis.com/css2?family=Michroma&family=Open+Sans:wght@400;600&display=swap" rel="stylesheet">
<style>
  :root {
    --backdrop: #e7e5e2;
    --card: #ffffff;
    --ink: #1d1d1d;
    --ink-soft: #3a3a3a;
    --accent: #e08a2a;
    --icon: #2e2e2e;
  }
  * { margin: 0; padding: 0; box-sizing: border-box; }
  html, body {
    width: 1200px; height: 997px; overflow: hidden;
    background: var(--backdrop);
    font-family: "Open Sans", Arial, sans-serif;
    color: var(--ink);
  }
  .sheet {
    width: 1200px; height: 997px;
    display: flex; flex-direction: column; align-items: center; justify-content: center;
    gap: 44px;
  }
  .card {
    width: 760px; height: 434px;
    background: var(--card);
    box-shadow: 0 6px 18px rgba(0,0,0,0.10);
    position: relative;
  }

  /* Back side */
  .card-back {
    display: flex; flex-direction: column; align-items: center; justify-content: center;
    gap: 70px;
  }
  .brand {
    display: flex; align-items: center; gap: 16px;
  }
  .brand-mark {
    width: 22px; height: 22px;
    border: 2px solid var(--ink);
  }
  .brand-name {
    font-size: 26px; font-weight: 600; letter-spacing: 0.14em;
    text-transform: uppercase; color: var(--ink);
    white-space: nowrap;
  }
  .back-web {
    font-size: 22px; letter-spacing: 0.04em; color: var(--ink);
  }

  /* Front side */
  .card-front .person {
    position: absolute; left: 70px; top: 110px;
  }
  .person-name {
    font-family: "Michroma", "Arial Black", sans-serif;
    font-size: 22px; letter-spacing: 0.08em; color: var(--accent);
    text-transform: uppercase; white-space: nowrap;
  }
  .person-title {
    font-size: 13px; color: var(--ink-soft); margin-top: 2px;
  }
  .contact-list {
    list-style: none; margin-top: 30px; margin-left: 28px;
    display: flex; flex-direction: column; gap: 11px;
  }
  .contact-item {
    display: flex; align-items: center; gap: 14px;
    font-size: 15px; color: var(--ink); white-space: nowrap;
  }
  .contact-icon { width: 22px; height: 22px; flex: none; }

  .divider {
    position: absolute; left: 430px; top: 70px;
    width: 1.5px; height: 170px;
    background: linear-gradient(var(--ink), rgba(0,0,0,0.2));
    transform: rotate(-32deg); transform-origin: top center;
  }
  .card-front .brand-block {
    position: absolute; right: 40px; top: 110px; width: 180px;
    display: flex; flex-direction: column; align-items: center; gap: 12px;
  }
  .brand-block .brand-name { font-size: 15px; }
  .brand-rule { width: 180px; height: 1.5px; background: var(--ink); }
</style>
</head>
<body>
<main class="sheet">

  <section class="card card-back" aria-label="Card back">
    <div class="brand">
      <span class="brand-mark" aria-hidden="true"></span>
      <span class="brand-name">Stonefield Custom Builders</span>
    </div>
    <p class="back-web">www.Stonefieldcustombuilders-example.com</p>
  </section>

  <section class="card card-front" aria-label="Card front">
    <div class="person">
      <h1 class="person-name">Marcus Tilley</h1>
      <p class="person-title">CEO/Managing Director</p>
      <ul class="contact-list">
        <li class="contact-item">
          <svg class="contact-icon" viewBox="0 0 24 24" aria-hidden="true"><rect width="24" height="24" rx="5" fill="var(--icon)"/><path d="M8 6.5c.6-.5 1.3-.4 1.7.2l1 1.6c.3.5.2 1.1-.2 1.4l-.8.6c.6 1.4 1.600 2.5 3 3.2l.7-.8c.4-.4 1-.5 1.4-.2l1.6 1c.6.4.7 1.2.2 1.7l-.8.9c-.8.8-2.1.9-3.2.3-2.6-1.4-4.5-3.4-5.7-6-.5-1.1-.3-2.300.5-3.1z" fill="#fff"/></svg>
          <span>208 367 4120</span>
        </li>
        <li class="contact-item">
          <svg class="contact-icon" viewBox="0 0 24 24" aria-hidden="true"><rect width="24" height="24" rx="5" fill="var(--icon)"/><path d="M5 12l7-6 7 6M7.5 10.5V18h3.5v-4h2v4h3.5v-7.5" fill="none" stroke="#fff" stroke-width="1.6" stroke-linejoin="round"/></svg>
          <span>208 367 4120</span>
        </li>
        <li class="contact-item">
          <svg class="contact-icon" viewBox="0 0 24 24" aria-hidden="true"><rect x="3" y="6" width="18" height="12" fill="none" stroke="var(--icon)" stroke-width="1.6"/><path d="M3 6l9 7 9-7M3 18l6.5-6M21 18l-6.5-6" fill="none" stroke="var(--icon)" stroke-width="1.4"/></svg>
          <span>MarcusTilleySCB@mailbox-example.com</span>
        </li>
        <li class="contact-item">
          <svg class="contact-icon" viewBox="0 0 24 24" aria-hidden="true"><rect width="24" height="24" rx="5" fill="var(--icon)"/><circle cx="12" cy="12" r="6.5" fill="none" stroke="#fff" stroke-width="1.3"/><ellipse cx="12" cy="12" rx="3" ry="6.5" fill="none" stroke="#fff" stroke-width="1.1"/><path d="M5.5 12h13M6.5 9h11M6.5 15h11" stroke="#fff" stroke-width="1"/></svg>
          <span>Stonefieldcustombuilders-example.com</span>
        </li>
      </ul>
    </div>

    <span class="divider" aria-hidden="true"></span>

    <div class="brand-block">
      <span class="brand-mark" aria-hidden="true"></span>
      <span class="brand-name">Stonefield</span>
      <span class="brand-rule" aria-hidden="true"></span>
      <span class="brand-name">Custom Builders</span>
    </div>
  </section>

</main>
</body>
</html>
```